Service Plans and Offerings - One Page

We are looking for an 8.5 x 11 one page in a portrait orientation that advertises our product and service offerings on one side and our logo and a slogan, "Reliable Managed IT Services & Support" - "TALMERO is ready to earn your trust" on the other with TALMERO contact information.

This brochure would be left at prospect client's business, so it needs to be inviting, professional, and clear.

Attached is one excel sheet with 4 columns representing our Service Plans and Offerings (Ideas on the descriptive names for the different service offering level is welcome) that we would like you to use for inspiration for the written content in the handout.

The brochure should have the TALMERO contact information on the bottom of the services description page and on the other side of the page (not necessary located at bottom). TALMERO contact information (email, phone, website) will provided to contest winner.

Please be creative with both the content and the design.

Target Market(s)

Small to medium companies with 5-50 seats.

Industry/Entity Type

Information Technology (IT) Managed Service Provider

Font styles to use
Serif

Colors
0094D4
00A9DD
6FCCEA
C7EBF8
E9F6FB

Requirements
Must have
• Clear and professional representation of TALMERO Product Services Plans and easy to read TALMERO contact information.

```html
<!DOCTYPE html>
<html lang="en">
<head>
<meta charset="utf-8">
<title>TALMERO – Service Plans and Offerings</title>
<link rel="stylesheet" href="https://fonts.googleapis.com/css2?family=Work+Sans:wght@400;500;600;700;800;900&display=swap">
<style>
  :root{
    --stage:#dcdcdc;
    --ink:#111111;
    --paper:#ffffff;
    --soft:#f3f3f3;
    --label-stripe:#ececec;
    --bronze:#8cc63f;
    --bronze-tint:#e3f1cf;
    --bronze-tint-2:#eef7e3;
    --silver:#2a9a4c;
    --silver-tint:#c9e6cf;
    --silver-tint-2:#dcefdf;
    --gold:#5c2d91;
    --gold-tint:#d9cbe8;
    --gold-tint-2:#e7ddf1;
    --plat:#1ea7e1;
    --plat-tint:#bfe6f6;
    --plat-tint-2:#d8f0fa;
    --star-off:#d9d9d9;
    --night:#0f0f0f;
    --art-light:#e6e6ee;
    --art-mid:#b9b6dc;
    --art-deep:#5c57b8;
  }
  *{box-sizing:border-box;margin:0;padding:0}
  html,body{width:1200px;height:900px;overflow:hidden}
  body{background:var(--stage);font-family:"Work Sans",Arial,sans-serif;color:var(--ink);
    display:flex;align-items:center;justify-content:center;gap:24px}
  .page{width:572px;height:740px;position:relative;box-shadow:0 6px 18px rgba(0,0,0,.18)}

  /* ---------- Plans side ---------- */
  .plans{background:var(--paper);padding:22px 22px 20px}
  .plan-head,.row{display:grid;grid-template-columns:216px repeat(4,1fr);column-gap:4px}
  .plan-head{height:118px}
  .sheet-title{align-self:end;background:var(--soft);padding:8px 10px 8px;margin-bottom:6px;margin-right:8px;
    font-weight:900;font-size:24px;line-height:.95;letter-spacing:.5px;text-transform:uppercase}
  .tier{display:flex;flex-direction:column;align-items:center;text-align:center;padding-bottom:6px;border-radius:8px 8px 0 0}
  .tier .pill{width:100%;border-radius:10px;color:#fff;font-weight:700;font-size:11px;padding:3px 0}
  .tier .trust{font-weight:700;font-size:10px;margin-top:5px;letter-spacing:.5px}
  .tier .stars{font-size:12px;line-height:1;letter-spacing:1px}
  .tier .stars .off{color:var(--star-off)}
  .tier .name{font-weight:800;font-size:10px;margin-top:8px;letter-spacing:.5px}
  .tier .price{font-weight:800;font-size:22px;background:#fff;padding:0 5px;border-radius:4px;margin-top:1px;line-height:1.1}
  .tier-bronze{background:linear-gradient(var(--paper),var(--bronze-tint-2))}
  .tier-bronze .pill{background:var(--bronze)} .tier-bronze .trust,.tier-bronze .stars,.tier-bronze .price{color:var(--bronze)}
  .tier-silver{background:linear-gradient(var(--paper),var(--silver-tint-2))}
  .tier-silver .pill{background:var(--silver)} .tier-silver .trust,.tier-silver .stars,.tier-silver .price{color:var(--silver)}
  .tier-gold{background:linear-gradient(var(--paper),var(--gold-tint-2))}
  .tier-gold .pill{background:var(--gold)} .tier-gold .trust,.tier-gold .stars,.tier-gold .price{color:var(--gold)}
  .tier-plat{background:linear-gradient(var(--paper),var(--plat-tint-2))}
  .tier-plat .pill{background:var(--plat)} .tier-plat .trust,.tier-plat .stars,.tier-plat .price{color:var(--plat)}

  .row{height:17px;font-size:9px;align-items:stretch}
  .row .label{display:flex;align-items:center;padding-left:24px;background:var(--label-stripe);margin-right:8px;white-space:nowrap}
  .row:nth-child(even) .label{background:var(--soft)}
  .row.category .label{background:none;padding-left:0;font-weight:800;font-size:12px;gap:6px}
  .row.category .label svg{width:14px;height:14px}
  .cell{display:flex;align-items:center;justify-content:center;font-weight:700;font-size:11px}
  .bronze{background:var(--bronze-tint)} .row:nth-child(even) .bronze{background:var(--bronze-tint-2)}
  .silver{background:var(--silver-tint)} .row:nth-child(even) .silver{background:var(--silver-tint-2)}
  .gold{background:var(--gold-tint)} .row:nth-child(even) .gold{background:var(--gold-tint-2)}
  .plat{background:var(--plat-tint)} .row:nth-child(even) .plat{background:var(--plat-tint-2)}

  /* ---------- Cover side ---------- */
  .cover{background:var(--night);color:#fff;padding:56px 56px}
  .cover-art{width:380px;height:330px;margin:0 auto;border-radius:14px;
    background:linear-gradient(150deg,var(--art-light) 0%,var(--art-mid) 60%,var(--art-deep) 100%)}
  .rule{height:1px;background:#fff;opacity:.85}
  .cover .rule.top{margin-top:44px}
  .headline{font-weight:800;font-size:34px;line-height:1.12;margin:24px 0 10px}
  .slogan{font-size:13px;letter-spacing:.6px;margin-bottom:24px}
  .contact{margin-top:24px;font-size:13px;letter-spacing:2px;line-height:1.7;text-transform:uppercase}
</style>
</head>
<body>

<section class="page cover">
  <div class="cover-art" role="img" aria-label="Illustration of a stylised head in profile with circuit lines and floating message cards"></div>
  <div class="rule top"></div>
  <h1 class="headline">Reliable Managed<br>IT Services &amp; Support</h1>
  <p class="slogan">TALMERO is ready to earn your trust</p>
  <div class="rule"></div>
  <p class="contact">0198 765 43210 &nbsp;|&nbsp; hello@talmero-it.com<br>talmero-it.com</p>
</section>

<section class="page plans">
  <header class="plan-head">
    <h2 class="sheet-title">Service<br>Plans and<br>Offerings</h2>
    <div class="tier tier-bronze"><span class="pill">Economic</span><span class="trust">TRUST</span><span class="stars">★<span class="off">★★★</span></span><span class="name">BRONZE</span><span class="price">$50</span></div>
    <div class="tier tier-silver"><span class="pill">Middle</span><span class="trust">TRUST</span><span class="stars">★★<span class="off">★★</span></span><span class="name">SILVER</span><span class="price">$89</span></div>
    <div class="tier tier-gold"><span class="pill">High</span><span class="trust">TRUST</span><span class="stars">★★★<span class="off">★</span></span><span class="name">GOLD</span><span class="price">$119</span></div>
    <div class="tier tier-plat"><span class="pill">Complete</span><span class="trust">TRUST</span><span class="stars">★★★★</span><span class="name">PLATINUM</span><span class="price">$145</span></div>
  </header>

  <div class="matrix">
    <div class="row category"><span class="label"><svg viewBox="0 0 14 14"><rect x="1" y="3" width="12" height="9" fill="#111"/><rect x="3" y="5" width="3" height="2" fill="#fff"/><rect x="8" y="8" width="3" height="2" fill="#fff"/></svg>Fortify</span><span class="cell bronze"></span><span class="cell silver"></span><span class="cell gold"></span><span class="cell plat"></span></div>
    <div class="row"><span class="label">Managed Firewall</span><span class="cell bronze"></span><span class="cell silver">×</span><span class="cell gold">×</span><span class="cell plat">×</span></div>
    <div class="row"><span class="label">AI-Based Next Gen Anti-Virus</span><span class="cell bronze"></span><span class="cell silver"></span><span class="cell gold">×</span><span class="cell plat">×</span></div>
    <div class="row"><span class="label">Traditional AV</span><span class="cell bronze">×</span><span class="cell silver">×</span><span class="cell gold"></span><span class="cell plat"></span></div>
    <div class="row"><span class="label">24/7 Security Operations Centre</span><span class="cell bronze"></span><span class="cell silver"></span><span class="cell gold">×</span><span class="cell plat">×</span></div>

    <div class="row category"><span class="label"><svg viewBox="0 0 14 14"><rect x="1" y="9" width="3" height="4" fill="#111"/><rect x="5" y="6" width="3" height="7" fill="#111"/><rect x="9" y="2" width="3" height="11" fill="#111"/></svg>Foundation</span><span class="cell bronze"></span><span class="cell silver"></span><span class="cell gold"></span><span class="cell plat"></span></div>
    <div class="row"><span class="label">24/7 Monitoring</span><span class="cell bronze">×</span><span class="cell silver">×</span><span class="cell gold">×</span><span class="cell plat">×</span></div>
    <div class="row"><span class="label">Security Patching</span><span class="cell bronze">×</span><span class="cell silver">×</span><span class="cell gold">×</span><span class="cell plat">×</span></div>
    <div class="row"><span class="label">Application Updates</span><span class="cell bronze">×</span><span class="cell silver">×</span><span class="cell gold">×</span><span class="cell plat">×</span></div>
    <div class="row"><span class="label">Pro-active Maintenance</span><span class="cell bronze">×</span><span class="cell silver">×</span><span class="cell gold">×</span><span class="cell plat">×</span></div>

    <div class="row category"><span class="label"><svg viewBox="0 0 14 14"><rect x="2" y="1" width="10" height="12" rx="2" fill="none" stroke="#111" stroke-width="2"/><rect x="5" y="4" width="4" height="3" fill="#111"/></svg>Backups</span><span class="cell bronze"></span><span class="cell silver"></span><span class="cell gold"></span><span class="cell plat"></span></div>
    <div class="row"><span class="label">Offsite Backups</span><span class="cell bronze"></span><span class="cell silver"></span><span class="cell gold">×</span><span class="cell plat">×</span></div>
    <div class="row"><span class="label">Email Backups</span><span class="cell bronze"></span><span class="cell silver">×</span><span class="cell gold">×</span><span class="cell plat">×</span></div>
    <div class="row"><span class="label">Onsite Backups</span><span class="cell bronze">×</span><span class="cell silver">×</span><span class="cell gold">×</span><span class="cell plat">×</span></div>

    <div class="row category"><span class="label"><svg viewBox="0 0 14 14"><polygon points="7,1 8.8,5.2 13,5.5 9.8,8.4 10.8,13 7,10.6 3.2,13 4.2,8.4 1,5.5 5.2,5.2" fill="#111"/></svg>Vigilence</span><span class="cell bronze"></span><span class="cell silver"></span><span class="cell gold"></span><span class="cell plat"></span></div>
    <div class="row"><span class="label">Dark Web Monitoring</span><span class="cell bronze"></span><span class="cell silver"></span><span class="cell gold">×</span><span class="cell plat">×</span></div>
    <div class="row"><span class="label">Annual User Training</span><span class="cell bronze"></span><span class="cell silver">×</span><span class="cell gold">×</span><span class="cell plat">×</span></div>

    <div class="row category"><span class="label"><svg viewBox="0 0 14 14"><rect x="5" y="1" width="4" height="4" fill="#111"/><rect x="1" y="9" width="4" height="4" fill="#111"/><rect x="9" y="9" width="4" height="4" fill="#111"/><path d="M7 5v2H3v2M7 7h4v2" fill="none" stroke="#111" stroke-width="1.2"/></svg>Strategy</span><span class="cell bronze"></span><span class="cell silver"></span><span class="cell gold"></span><span class="cell plat"></span></div>
    <div class="row"><span class="label">IT Strategic Planning</span><span class="cell bronze"></span><span class="cell silver"></span><span class="cell gold"></span><span class="cell plat">×</span></div>
    <div class="row"><span class="label">Technology Roadmap</span><span class="cell bronze"></span><span class="cell silver"></span><span class="cell gold"></span><span class="cell plat">×</span></div>
    <div class="row"><span class="label">Disaster Recovery Planning</span><span class="cell bronze"></span><span class="cell silver"></span><span class="cell gold">×</span><span class="cell plat">×</span></div>

    <div class="row category"><span class="label"><svg viewBox="0 0 14 14"><path d="M2 1h7l3 3v9H2z" fill="none" stroke="#111" stroke-width="1.6"/><path d="M4 6h6M4 8h6M4 10h4" stroke="#111" stroke-width="1.2"/></svg>Reports</span><span class="cell bronze"></span><span class="cell silver"></span><span class="cell gold"></span><span class="cell plat"></span></div>
    <div class="row"><span class="label">Inventory and Asset Reporting</span><span class="cell bronze"></span><span class="cell silver"></span><span class="cell gold">×</span><span class="cell plat">×</span></div>
    <div class="row"><span class="label">Service Delivery Reports</span><span class="cell bronze">×</span><span class="cell silver">×</span><span class="cell gold">×</span><span class="cell plat">×</span></div>

    <div class="row category"><span class="label"><svg viewBox="0 0 14 14"><circle cx="8" cy="6" r="4" fill="none" stroke="#111" stroke-width="2"/><path d="M5 9l-4 4" stroke="#111" stroke-width="2"/></svg>Clarity</span><span class="cell bronze"></span><span class="cell silver"></span><span class="cell gold"></span><span class="cell plat"></span></div>
    <div class="row"><span class="label">Simplified Billing</span><span class="cell bronze">×</span><span class="cell silver">×</span><span class="cell gold">×</span><span class="cell plat">×</span></div>
    <div class="row"><span class="label">Lifecycle Planning</span><span class="cell bronze"></span><span class="cell silver">×</span><span class="cell gold">×</span><span class="cell plat">×</span></div>
    <div class="row"><span class="label">Budgeting</span><span class="cell bronze"></span><span class="cell silver"></span><span class="cell gold">×</span><span class="cell plat">×</span></div>
    <div class="row"><span class="label">Vendor Liason</span><span class="cell bronze"></span><span class="cell silver"></span><span class="cell gold">×</span><span class="cell plat">×</span></div>
    <div class="row"><span class="label">Procurement</span><span class="cell bronze"></span><span class="cell silver"></span><span class="cell gold">×</span><span class="cell plat">×</span></div>

    <div class="row category"><span class="label"><svg viewBox="0 0 14 14"><circle cx="7" cy="7" r="6" fill="#111"/><circle cx="7" cy="5.5" r="2" fill="#fff"/><path d="M3.5 11a3.5 3 0 0 1 7 0" fill="#fff"/></svg>User Support</span><span class="cell bronze"></span><span class="cell silver"></span><span class="cell gold"></span><span class="cell plat"></span></div>
    <div class="row"><span class="label">Unlimited Support</span><span class="cell bronze">×</span><span class="cell silver">×</span><span class="cell gold">×</span><span class="cell plat">×</span></div>
  </div>
</section>

</body>
</html>
```